Update Business Card Design

I'm looking to update my business cards. Attached is a photo of the current design. I like the black side so that does not have to be update. The white side needs to be updated. I want the design to be modern and minimalistic.
I am a lawyer and my firm's website is www.harborstonepartners.com (for reference).
My firm's logo has a horizontal version (which is on the black side of the card) and a vertical version (on the white side). I would prefer to keep the vertical version on the white side and horizontal version on the black side (the logo files are attached).

I am open to redesigning the black side also. I would like one side to have the horizontal logo and the other to have the vertical logo.

Went on vacation/holiday

```html
<!DOCTYPE html>
<html lang="en">
<head>
<meta charset="utf-8">
<title>Harborstone Partners – Business Card</title>
<link href="https://fonts.googleapis.com/css2?family=Cinzel:wght@400;700&family=Arimo:wght@400&display=swap" rel="stylesheet">
<style>
  :root{
    --backdrop:#474747;
    --ink-black:#1a1a1a;
    --deep-black:#020202;
    --brand-blue:#10b2d8;
    --paper:#f3f4f6;
    --text-grey:#3c3c3c;
    --bar-grey:#454648;
    --white:#ffffff;
  }
  *{margin:0;padding:0;box-sizing:border-box}
  html,body{width:1200px;height:963px;overflow:hidden;background:var(--backdrop)}
  .canvas{position:relative;width:1200px;height:963px}

  .card{position:absolute;top:174px;width:318px;height:556px;overflow:hidden}
  .card-front{left:221px;background:var(--paper)}
  .card-back{left:636px;background:var(--deep-black)}

  .front-shape{position:absolute;inset:0;width:100%;height:100%}

  .firm-name{
    position:absolute;left:0;top:176px;width:200px;text-align:center;
    font-family:"Cinzel",serif;font-weight:400;color:var(--brand-blue);
    font-size:22px;line-height:1.2;letter-spacing:.5px;
  }

  .contact{position:absolute;right:57px;text-align:right;font-family:"Arimo",sans-serif;color:var(--text-grey);font-size:13px;line-height:17px;white-space:nowrap}
  .role{top:342px;right:31px;font-size:14px}
  .person{position:absolute;right:30px;top:362px;font-family:"Cinzel",serif;font-weight:700;font-size:19px;color:var(--brand-blue);letter-spacing:.3px;white-space:nowrap}
  .address{top:397px}
  .phone-main{top:438px}
  .phone-mobile{top:461px}
  .phone-fax{top:484px}
  .email{top:508px;font-size:12.5px}

  .icon{position:absolute;left:269px;width:19px;height:19px}
  .icon-pin{top:398px}
  .icon-phone{top:437px}
  .icon-mobile{top:460px}
  .icon-fax{top:483px}
  .icon-mail{top:507px}

  .web-bar{position:absolute;left:0;bottom:0;width:100%;height:21px;background:var(--bar-grey);
    font-family:"Arimo",sans-serif;font-size:13px;color:var(--white);text-align:right;padding-right:33px;line-height:21px}

  .back-name{
    position:absolute;left:160px;top:262px;transform:translate(-50%,-50%) rotate(-90deg);
    font-family:"Cinzel",serif;font-weight:400;color:var(--brand-blue);
    font-size:34px;line-height:1.25;white-space:nowrap;text-align:center;
  }
  .back-web{
    position:absolute;left:245px;top:279px;transform:translate(-50%,-50%) rotate(-90deg);
    font-family:"Cinzel",serif;font-weight:700;color:var(--white);
    font-size:13px;letter-spacing:3px;white-space:nowrap;
  }
</style>
</head>
<body>
<div class="canvas">

  <section class="card card-front">
    <svg class="front-shape" viewBox="0 0 398 698" preserveAspectRatio="none" aria-hidden="true">
      <rect x="0" y="0" width="398" height="402" fill="var(--brand-blue)"/>
      <path d="M0 0 H398 V20 C370 210 270 370 80 374 C45 375 20 372 0 368 Z" fill="var(--ink-black)"/>
    </svg>

    <div class="firm-name">HARBORSTONE<br>PARTNERS</div>

    <div class="contact role">Attorney at Law</div>
    <div class="person">DANIEL MERCER</div>
    <div class="contact address">218 Linden Avenue, Suite 410<br>Westbrook, CA 90415</div>
    <div class="contact phone-main">555.214.3081</div>
    <div class="contact phone-mobile">555.482.6157</div>
    <div class="contact phone-fax">555.309.7724</div>
    <div class="contact email">daniel@harborstonepartners.com</div>

    <svg class="icon icon-pin" viewBox="0 0 20 20" aria-hidden="true"><circle cx="10" cy="10" r="8.8" fill="none" stroke="var(--brand-blue)" stroke-width="1.5"/><path d="M10 15 C7 11 6.5 9.5 6.5 8.3 A3.5 3.5 0 0 1 13.5 8.3 C13.5 9.5 13 11 10 15Z" fill="none" stroke="var(--brand-blue)" stroke-width="1.3"/><circle cx="10" cy="8.3" r="1.2" fill="var(--brand-blue)"/></svg>
    <svg class="icon icon-phone" viewBox="0 0 20 20" aria-hidden="true"><circle cx="10" cy="10" r="8.8" fill="none" stroke="var(--brand-blue)" stroke-width="1.5"/><path d="M6.5 5.5 L8.3 5.2 L9.2 7.6 L8 8.6 C8.6 10 9.8 11.3 11.3 12 L12.3 10.8 L14.7 11.7 L14.4 13.5 C10 14 6 10 6.5 5.5Z" fill="var(--brand-blue)"/></svg>
    <svg class="icon icon-mobile" viewBox="0 0 20 20" aria-hidden="true"><circle cx="10" cy="10" r="8.8" fill="none" stroke="var(--brand-blue)" stroke-width="1.5"/><rect x="7.3" y="5" width="5.4" height="10" rx="1" fill="none" stroke="var(--brand-blue)" stroke-width="1.3"/><circle cx="10" cy="13.2" r=".6" fill="var(--brand-blue)"/></svg>
    <svg class="icon icon-fax" viewBox="0 0 20 20" aria-hidden="true"><circle cx="10" cy="10" r="8.8" fill="none" stroke="var(--brand-blue)" stroke-width="1.5"/><rect x="7.5" y="5.5" width="5" height="3" fill="var(--brand-blue)"/><rect x="5.5" y="8.5" width="9" height="4.5" rx=".8" fill="var(--brand-blue)"/><rect x="7.5" y="11.5" width="5" height="3" fill="var(--paper)" stroke="var(--brand-blue)" stroke-width="1"/></svg>
    <svg class="icon icon-mail" viewBox="0 0 20 20" aria-hidden="true"><circle cx="10" cy="10" r="8.8" fill="none" stroke="var(--brand-blue)" stroke-width="1.5"/><rect x="5.5" y="6.8" width="9" height="6.4" fill="var(--brand-blue)"/><path d="M5.5 6.8 L10 10.6 L14.5 6.8" fill="none" stroke="var(--paper)" stroke-width="1"/></svg>

    <div class="web-bar">www.harborstonepartners.com</div>
  </section>

  <section class="card card-back">
    <div class="back-name">HARBORSTONE<br>PARTNERS</div>
    <div class="back-web">WWW.HARBORSTONEPARTNERS.COM</div>
  </section>

</div>
</body>
</html>
```